Law firm website marketed direct to many individual clients

I need someone to design a very basic website for a law firm that will be very eye catching. It's going to be a single-paged, scrolling website with a small number of folds. I have uploaded a simple word document that outlines the basics of what I thought could be the layout, but I am open to suggestion on font, size, shades of color, organization, etc. etc. Essentially the website just needs to be a very efficient and visually appealing way of conveying some simple messages.

Target Market(s)

High volumes of individuals who have gotten into a car accident and then google on their phones a lawyer to hire to represent them.

Industry/Entity Type

Legal

Number of Pages Required

1 page

Font styles to use
Serif
Sans Serif

Colors
34a7d7
85cae6
0592cd

Requirements
Must have
• Must be bright and grab the users attention with color scheme and layout. The different sections should be done in such a way that they can fit entirely onto one smart phone or tablet screen.
Nice to have
• I'd like to try and see what it looks like if in the middle somewhere there is a fold that says "MEET YOUR ATTORNEYS" and includes individual photos of two attorneys, one on the left side and one on the right. And then a small bio section on them. I don't want the photos to include a square or rectangle background, I want the person in the photo to be superimposed on top of whatever pattern or background you have in the fold.
Should not have
• Do not want too much text. Anything more than 2 sentences in any single place is unacceptable.

```html
<!DOCTYPE html>
<html lang="en">
<head>
<meta charset="utf-8">
<title>Harborline Law Group</title>
<link href="https://fonts.googleapis.com/css2?family=Open+Sans:wght@300;400;600;700&display=swap" rel="stylesheet">
<style>
  :root {
    --brand: #0592cd;
    --brand-mid: #34a7d7;
    --brand-light: #85cae6;
    --hero-deep: #0a5f8e;
    --hero-bright: #1682b9;
    --band-deep: #1f6d92;
    --band-bright: #3a93bd;
    --ink: #25282f;
    --ink-soft: #555a62;
    --paper: #ffffff;
    --mist: #f2f2f2;
    --panel: #2a2d36;
  }
  * { box-sizing: border-box; margin: 0; padding: 0; }
  html, body { width: 1200px; height: 2476px; overflow: hidden; }
  body { font-family: "Open Sans", Arial, sans-serif; background: var(--paper); position: relative; color: var(--ink); }
  .abs { position: absolute; }
  .center { left: 0; width: 1200px; text-align: center; }

  /* header */
  .site-header { top: 0; left: 0; width: 1200px; height: 83px; background: var(--ink); }
  .brand-name { left: 125px; top: 12px; color: var(--brand-mid); font-weight: 700; font-size: 29px; line-height: 30px; text-align: center; letter-spacing: 0.5px; }
  .brand-name small { display: block; font-size: 21px; line-height: 24px; letter-spacing: 0; }
  .header-phone { left: 786px; top: 0; width: 312px; height: 83px; background: var(--brand); color: var(--paper); display: flex; align-items: center; justify-content: center; gap: 14px; font-weight: 600; font-size: 35px; }

  /* hero */
  .hero { top: 83px; left: 0; width: 1200px; height: 624px; background: linear-gradient(160deg, var(--hero-bright) 0%, var(--hero-deep) 55%, #0c6a9c 100%); color: var(--paper); }
  .hero-kicker { top: 115px; font-weight: 600; font-size: 30px; }
  .hero-title { top: 155px; font-weight: 300; font-size: 90px; line-height: 78px; letter-spacing: -1px; }
  .hero-title b { font-weight: 700; }
  .hero-rule { top: 333px; left: 512px; width: 154px; height: 4px; background: var(--paper); }
  .hero-call { top: 415px; font-size: 36px; }
  .hero-call b { font-weight: 700; }
  .btn { display: flex; align-items: center; justify-content: center; color: var(--paper); font-size: 22px; }
  .btn b { font-weight: 700; margin-left: 6px; }
  .btn-dark { background: #111; }
  .btn-brand { background: var(--brand); }
  .btn-ink { background: var(--ink); }
  .hero-btn { top: 478px; left: 464px; width: 253px; height: 52px; font-weight: 600; }

  /* features */
  .features { top: 707px; left: 0; width: 1200px; height: 366px; background: var(--mist); }
  .feature-card { top: 809px; width: 224px; height: 213px; background: var(--paper); border-bottom: 5px solid var(--brand); box-shadow: 0 2px 6px rgba(0,0,0,0.12); text-align: center; }
  .feature-icon { position: absolute; left: 61px; top: -43px; width: 102px; height: 102px; border-radius: 50%; background: var(--brand); display: flex; align-items: center; justify-content: center; }
  .feature-title { position: absolute; top: 81px; left: 0; width: 100%; color: var(--brand); font-weight: 700; font-size: 18px; line-height: 21px; }
  .feature-text { position: absolute; top: 132px; left: 12px; right: 12px; color: var(--ink-soft); font-size: 14px; line-height: 19px; }

  /* attorneys band */
  .attorney-band { top: 1073px; left: 0; width: 1200px; height: 875px; }
  .band-call { top: 1081px; left: 470px; width: 256px; height: 53px; }
  .section-title { top: 1300px; color: var(--paper); font-weight: 300; font-size: 33px; }
  .section-title b { font-weight: 700; }
  .section-rule { top: 1352px; left: 543px; width: 114px; height: 4px; background: var(--paper); }
  .portrait { top: 1403px; height: 314px; border-radius: 140px 140px 0 0; background: linear-gradient(180deg, rgba(210,220,228,0.55) 0%, rgba(40,44,54,0.85) 60%, #1d2028 100%); }
  .portrait-left { left: 190px; width: 297px; }
  .portrait-right { left: 721px; width: 278px; }
  .portrait-call { top: 1453px; left: 470px; width: 258px; height: 53px; }
  .bio-card { top: 1714px; width: 473px; height: 163px; background: var(--panel); border: 4px solid var(--brand-light); color: var(--paper); text-align: center; }
  .bio-name { margin-top: 22px; font-weight: 700; font-size: 18px; }
  .bio-rule { width: 52px; height: 3px; background: var(--brand-mid); margin: 12px auto 22px; }
  .bio-text { font-size: 13.5px; line-height: 20px; color: #d7dadf; padding: 0 40px; }

  /* info */
  .info-heading { top: 2022px; color: var(--brand); font-weight: 400; font-size: 27px; }
  .info-heading b { font-weight: 700; }
  .info-text { top: 2068px; font-size: 11.5px; line-height: 20px; color: var(--ink-soft); }
  .info-text em { font-style: normal; color: var(--brand); }
  .info-btn { top: 2176px; left: 464px; width: 257px; height: 54px; }

  /* footer */
  .site-footer { top: 2303px; left: 0; width: 1200px; height: 173px; background: var(--ink); border-top: 5px solid var(--brand); }
  .footer-divider { top: 2339px; height: 1px; background: #3a3e48; }
  .footer-brand { top: 2324px; color: var(--brand-mid); font-weight: 700; font-size: 21px; line-height: 22px; }
  .footer-brand small { display: block; font-size: 15px; line-height: 18px; }
  .footer-brand-rule { top: 2373px; left: 578px; width: 44px; height: 2px; background: #6a6f7a; }
  .footer-address { top: 2385px; color: var(--paper); font-size: 13.5px; line-height: 20px; }
  .footer-address b { font-weight: 700; }
</style>
</head>
<body>

<header class="site-header abs"></header>
<div class="brand-name abs">HARBORLINE<small>LAW GROUP</small></div>
<div class="header-phone abs">
  <svg width="20" height="32" viewBox="0 0 20 32" aria-hidden="true"><rect x="1.5" y="1.5" width="17" height="29" rx="3" fill="none" stroke="#25282f" stroke-width="3"/><rect x="4" y="5" width="12" height="19" fill="#25282f"/></svg>
  (504) 555-0187
</div>

<section class="hero abs"></section>
<div class="hero-kicker abs center" style="color:#fff">ACCIDENT?&nbsp; INJURED?</div>
<h1 class="hero-title abs center" style="color:#fff">YOUR <b>CASE</b><br>YOUR <b>MONEY</b></h1>
<div class="hero-rule abs"></div>
<div class="hero-call abs center" style="color:#fff">Call: <b>504-555-0187</b></div>
<div class="btn btn-dark hero-btn abs">LEARN MORE</div>

<section class="features abs"></section>

<svg class="attorney-band abs" width="1200" height="875" viewBox="0 0 1200 875" aria-hidden="true">
  <defs>
    <linearGradient id="bandFill" x1="0" y1="0" x2="1" y2="1">
      <stop offset="0" stop-color="#3a93bd"/>
      <stop offset="0.5" stop-color="#2d82ab"/>
      <stop offset="1" stop-color="#1f6d92"/>
    </linearGradient>
  </defs>
  <path d="M0 0 L600 157 L1200 0 L1200 875 L0 875 Z" fill="url(#bandFill)"/>
</svg>

<div class="feature-card abs" style="left:106px">
  <div class="feature-icon"><svg width="46" height="46" viewBox="0 0 46 46" aria-hidden="true"><path d="M6 22 L22 6 L38 6 L38 22 L22 38 Z" fill="#fff" transform="rotate(10 23 23)"/><circle cx="32" cy="12" r="3" fill="#0592cd"/><text x="21" y="29" font-family="Open Sans, sans-serif" font-weight="700" font-size="15" fill="#0592cd" text-anchor="middle">$</text></svg></div>
  <div class="feature-title">LOW FEES</div>
  <div class="feature-text">We charge less, so you keep more.</div>
</div>
<div class="feature-card abs" style="left:362px">
  <div class="feature-icon"><svg width="46" height="50" viewBox="0 0 46 50" aria-hidden="true"><circle cx="23" cy="13" r="10" fill="#fff"/><path d="M3 48 Q3 27 23 27 Q43 27 43 48 Z" fill="#fff"/><path d="M21 28 L25 28 L26 42 L23 46 L20 42 Z" fill="#0592cd"/></svg></div>
  <div class="feature-title">FREE CONSULTATION</div>
  <div class="feature-text">It's always free to<br>talk to us.</div>
</div>
<div class="feature-card abs" style="left:616px">
  <div class="feature-icon"><svg width="28" height="48" viewBox="0 0 28 48" aria-hidden="true"><rect x="2" y="2" width="24" height="44" rx="4" fill="none" stroke="#fff" stroke-width="3"/><rect x="6" y="8" width="16" height="28" fill="#fff"/><circle cx="14" cy="41" r="2" fill="#fff"/></svg></div>
  <div class="feature-title">GET STARTED USING<br>ONLY YOUR PHONE</div>
  <div class="feature-text">No need to come to the office, sign up using your phone.</div>
</div>
<div class="feature-card abs" style="left:872px">
  <div class="feature-icon"><svg width="50" height="44" viewBox="0 0 50 44" aria-hidden="true"><path d="M4 4 H32 V24 H14 L6 31 V24 H4 Z" fill="#fff"/><path d="M36 12 H46 V32 H44 V39 L37 32 H18 V28 H36 Z" fill="#fff"/></svg></div>
  <div class="feature-title">SPEAK DIRECTLY<br>TO A LAWYER</div>
  <div class="feature-text">No staff screening. Talk right to a lawyer on your first call.</div>
</div>

<div class="btn btn-brand band-call abs">CALL <b>504-555-0187</b></div>

<h2 class="section-title abs center">MEET YOUR <b>ATTORNEYS</b></h2>
<div class="section-rule abs"></div>

<div class="portrait portrait-left abs" role="img" aria-label="Cut-out portrait of the first attorney in a dark suit, arms crossed"></div>
<div class="portrait portrait-right abs" role="img" aria-label="Cut-out portrait of the second attorney in a dark suit giving a thumbs up"></div>
<div class="btn btn-ink portrait-call abs">CALL <b>504-555-0187</b></div>

<div class="bio-card abs" style="left:107px">
  <div class="bio-name">LAWYER NAME</div>
  <div class="bio-rule"></div>
  <p class="bio-text">Lorem ipsum dolor sit amet, consectetur adipisicing elit, sed do eiusmod tempor incididunt ut labore et dolore magna aliqua.</p>
</div>
<div class="bio-card abs" style="left:624px">
  <div class="bio-name">LAWYER NAME</div>
  <div class="bio-rule"></div>
  <p class="bio-text">Lorem ipsum dolor sit amet, consectetur adipisicing elit, sed do eiusmod tempor incididunt ut labore et dolore magna aliqua.</p>
</div>

<h3 class="info-heading abs" style="left:198px"><b>NO FEE</b> UNLESS WE WIN</h3>
<p class="info-text abs" style="left:198px;width:380px">We don't get paid unless you get paid. It's as simple as that. We let our results do the talking for us.</p>
<h3 class="info-heading abs" style="left:616px"><b>QUESTIONS</b> ABOUT ANYTHING?</h3>
<p class="info-text abs" style="left:616px;width:520px">We're here to help. Feel free to call us at <em>504-555-0187</em> to speak to one of our attorneys. With extensive experience in helping clients get the results that they want, our team is always just a phone call away.</p>
<div class="btn btn-brand info-btn abs">CALL <b>504-555-0187</b></div>

<footer class="site-footer abs"></footer>
<div class="footer-divider abs" style="left:0;width:520px"></div>
<div class="footer-divider abs" style="left:680px;width:520px"></div>
<div class="footer-brand abs center">HARBORLINE<small>LAW GROUP</small></div>
<div class="footer-brand-rule abs"></div>
<address class="footer-address abs center" style="font-style:normal">Riverside Office Suite<br>New Orleans, LA 70112<br><b>504-555-0187</b></address>

</body>
</html>
```